電子書籍(ビジネス書)のブックデザインをお願いします。

■本のタイトル
「ひだまり工房で毎日笑顔のまま確かに伸ばす手づくり教室繁盛術」

親しみやすく、明るく、でもきちんとしたビジネスのイメージです。
電子書籍は画像が小さいので、できるだけ認識しやすい文字でお願いします。

■帯
元・40代公務員が見つけた、自分らしく時間もお金も手に入れるたった3つの思考法

■読者全員プレゼント
「毎朝がときめく三分間ノート整理術入門講座ガイド」動画

■著者  MARISA
■肩書 ずっと続く笑顔の教室づくりアドバイザー

■色の指定などはありません。
明るい、親しみやすい、きちんとしてる
女性が楽しそうに稼いでいる感じのイラストなどが入ってもいいです。

■選定確約です。

■参考に書籍の原稿を添付します。

その他何かご不明な点がございましたら、お気軽にご質問下さい。
よろしくお願いいたします。
ランサーの皆さま、
ご提案いただきありがとうございます。

記載内容に変更があります。

肩書きを
「おうちサロン開業経営改善コンサルタント」
に変更します。

既にデザインを提出してくださっている方は
そのまま変更前の肩書で大丈夫です。
(採用時に修正をお願いします)

これからご提案くださるランサー様は
変更後の肩書でよろしくお願いします。

引き続きご提案をお待ちしております。
ありがとうございます。
ランサーの皆さま、ご提案ありがとうございました。

検討させていただき、近日中にご報告いたします。
採用のデザインでも修正等をお願いすると思いますので、よろしくお願いします。

採用のランサー様、2位のランサー様には別途ご連絡します。

ありがとうございました!

提案締め切り後に仕様が少し変わり
私の写真をいれていただきました。

選定のご提案は、写真の配置と全体の濃淡のバランスが良く
タイトルや帯の文字が小さい画面でもはっきり見えるので
見栄えを優先してこちらの提案に決定いたしました。

次点の方もとても華やか素敵で
どちらも満足のいくご提案だったので最後まで迷いましたが、
ビジネス書ということ少し落ち着いた方になりました。

何度も修正いただいたランサー様には感謝します。

スタッフからもとても好評です。
ありがとうございました。

この度はたくさんの素敵なご提案をいただき
誠にありがとうございました。

どれもこちらの要望をしっかり反映していただき
王道なものから個性的なものまでいろいろなデザインで
クオリティの高いものをご提案いただいて、すごく迷いました。

本の内容をしっかりご理解いただいてのご提案が多くて
とても嬉しかったです。

今回選定できなかったランサーの皆さま
本当にありがとうございました。

また機会がありましたら、ぜひよろしくお願いします。

ありがとうございました。

```html
<!DOCTYPE html>
<html lang="ja">
<head>
<meta charset="utf-8">
<title>ひだまり工房で毎日笑顔のまま確かに伸ばす手づくり教室繁盛術</title>
<link rel="stylesheet" href="https://fonts.googleapis.com/css2?family=M+PLUS+Rounded+1c:wght@500;700;800&display=swap">
<style>
  :root {
    --pink-bg: #f6bcc2;
    --pink-stripe: #f2aeb6;
    --pink-accent: #e8517a;
    --brown: #5b3b2c;
    --white: #ffffff;
    --art-a: #f9e2d0;
    --art-b: #f2c7b4;
  }
  * { margin: 0; padding: 0; box-sizing: border-box; }
  html, body { width: 752px; height: 1200px; overflow: hidden; }
  body { font-family: "M PLUS Rounded 1c", sans-serif; color: var(--brown); }

  .cover {
    position: relative; width: 752px; height: 1200px; overflow: hidden;
    background: repeating-linear-gradient(90deg, var(--pink-bg) 0 18px, var(--pink-stripe) 18px 36px);
  }
  .house-frame { position: absolute; inset: 0; }

  .title-block { position: absolute; top: 228px; left: 0; width: 752px; text-align: center; }
  .title-lead { font-size: 32px; font-weight: 700; letter-spacing: 1px; }
  .title-main { margin-top: 12px; font-size: 80px; font-weight: 800; line-height: 1.12; letter-spacing: 2px; }

  .author-title {
    position: absolute; top: 598px; left: 200px; width: 352px; height: 72px;
    background: var(--white); border-radius: 36px;
    display: flex; flex-direction: column; justify-content: center; align-items: center;
    font-size: 22px; font-weight: 700; line-height: 1.3;
  }
  .author-name { position: absolute; top: 700px; left: 0; width: 752px; text-align: center; font-size: 38px; font-weight: 800; letter-spacing: 2px; }
  .author-name small { font-size: 26px; margin-left: 8px; }

  .obi { position: absolute; top: 812px; left: 0; width: 752px; height: 388px; background: var(--white); }
  .author-art {
    position: absolute; top: 700px; left: 520px; width: 232px; height: 410px;
    background: linear-gradient(180deg, var(--art-a), var(--art-b));
    border-radius: 110px 110px 0 0;
  }
  .obi-copy { position: absolute; top: 846px; left: 26px; font-weight: 800; }
  .obi-copy .line1 { font-size: 38px; }
  .obi-copy .line2, .obi-copy .line3 { font-size: 50px; line-height: 1.3; }
  .obi-copy .hl { color: var(--pink-accent); }
  .obi-copy .line4 { font-size: 54px; display: flex; align-items: center; gap: 12px; margin-top: 4px; }
  .just-tag { font-size: 24px; border: 3px solid var(--brown); border-radius: 18px; padding: 2px 12px; }

  .gift { position: absolute; top: 1112px; left: 0; width: 752px; height: 88px; background: var(--white); border-top: 3px solid var(--pink-stripe); display: flex; align-items: center; }
  .gift-badge {
    margin-left: 14px; width: 98px; height: 72px; background: var(--pink-accent); color: var(--white);
    border-radius: 10px; font-size: 19px; font-weight: 800; line-height: 1.2;
    display: flex; align-items: center; justify-content: center; text-align: center;
  }
  .gift-text { margin-left: 16px; font-size: 27px; font-weight: 800; line-height: 1.25; }
  .gift-text .hl { color: var(--pink-accent); }
</style>
</head>
<body>
<main class="cover">
  <svg class="house-frame" width="752" height="1200" viewBox="0 0 752 1200" aria-hidden="true">
    <polyline points="30,328 376,52 722,328" fill="none" stroke="var(--white)" stroke-width="9" stroke-linejoin="round" stroke-linecap="round"/>
    <line x1="108" y1="266" x2="108" y2="812" stroke="var(--white)" stroke-width="9" stroke-linecap="round"/>
    <line x1="644" y1="266" x2="644" y2="812" stroke="var(--white)" stroke-width="9" stroke-linecap="round"/>
  </svg>

  <header class="title-block">
    <p class="title-lead">ひだまり工房で毎日笑顔のまま</p>
    <h1 class="title-main">確かに伸ばす<br>手づくり教室<br>繁盛術</h1>
  </header>

  <p class="author-title"><span>ずっと続く笑顔の</span><span>教室づくりアドバイザー</span></p>
  <p class="author-name">MARISA<small>著</small></p>

  <section class="obi"></section>
  <div class="author-art" role="img" aria-label="笑顔で手を合わせる著者のイラスト"></div>

  <div class="obi-copy">
    <p class="line1">元・<span class="hl">40代公務員</span>が見つけた、</p>
    <p class="line2">自分らしく<span class="hl">時間</span>も</p>
    <p class="line3"><span class="hl">お金</span>も手に入れる</p>
    <p class="line4"><span class="just-tag">たった</span><span class="hl">3つの思考法</span></p>
  </div>

  <footer class="gift">
    <p class="gift-badge">読者全員<br>プレゼント</p>
    <p class="gift-text">「毎朝がときめく<span class="hl">三分間</span><br>ノート整理術入門講座ガイド」動画</p>
  </footer>
</main>
</body>
</html>
```